Elegant & Eye-Catching Brochure- Photo Booth Rentals

We rent photo booths for weddings, sweet 16's, parties, mitzvah's, school and corporate events and we would like to create a vibrant and fun, yet professional brochure to be attractive to the entire spectrum of potential clients. The brochure will be the standard tri-fold style (8.5"x11") and will have 3 inside panels and 3 outside panels.

Ideally this brochure would be elegant, classy, and professional, but still vibrant and fun. We have many colorful images that convey the quality of our photos and options, we want to highlight that aspect, but also would like to maintain that we are a great selection for weddings. Thus we stress the classy yet fun aspect of this project. Also, it would be preferable to use legible and interesting, but clear fonts. Clean and less cluttered is also a plus, but by all means just do what you think looks best.

Attached are the photos that we have available and fit our goals. There is no need to use them all, but if possible please stress the great range of options and the lovely clean wedding shots. Blue, White, Silver and a splash of pink have been used in the past for our logo, site, business cards, and older brochures so those are the preferred colors for this brochure. This brochure should trend feminine. Most of our clients are brides and mothers so that should be taken into consideration, but only to a point so that we don't close ourselves off to anyone.

I am attaching a logo, some photos strips, single shots, and instructions on the actual wording. Please let me know if you need anything else. Thank you in advance.
Updates

Target Market(s)

most of our clients are female, but the brochure shouldn't be so feminine as to dissuade males from becoming clients

Industry/Entity Type

School

Colors
f9d9e8
ffffff
f0f0f0
86cae7

Requirements
Nice to have
• A way of fitting in a variety of colorful photos to highlight our range, but while still maintaining a clean and ordered look.

```html
<!DOCTYPE html>
<html lang="en">
<head>
<meta charset="utf-8">
<title>Photo Booth Rentals – Tri-fold Inside Spread</title>
<link href="https://fonts.googleapis.com/css2?family=Montserrat:wght@400;700&family=Parisienne&display=swap" rel="stylesheet">
<style>
  :root {
    --canvas: #e6e8ea;
    --paper: #c6e4ec;
    --paper-deep: #b5dae5;
    --heading: #1b8fd2;
    --script: #2a8cc4;
    --body: #262a2c;
    --ribbon: #f29bc0;
    --banner: #8a8f94;
    --photo-frame: #ffffff;
  }
  * { margin: 0; padding: 0; box-sizing: border-box; }
  html, body { width: 1200px; height: 1000px; overflow: hidden; background: var(--canvas); }
  .spread {
    position: absolute; left: 68px; top: 90px; width: 1062px; height: 818px;
    background: linear-gradient(90deg, var(--paper) 0%, var(--paper-deep) 33.3%, var(--paper) 33.4%, var(--paper-deep) 66.6%, var(--paper) 66.7%, var(--paper-deep) 100%);
    font-family: "Montserrat", Arial, sans-serif; color: var(--body);
  }
  .panel { position: absolute; top: 0; width: 354px; height: 818px; }
  .panel-left { left: 0; }
  .panel-mid { left: 354px; padding: 21px 14px 0 24px; }
  .panel-right { left: 708px; padding: 21px 12px 0 17px; }
  h2 {
    font-family: "Montserrat", Arial, sans-serif; font-weight: 700; color: var(--heading);
    font-size: 17px; line-height: 22px; text-transform: uppercase;
  }
  h3 {
    font-family: "Parisienne", cursive; font-weight: 400; color: var(--script);
    font-size: 20px; line-height: 24px; margin-top: 16px;
  }
  p, li { font-size: 11.4px; line-height: 14.6px; }
  ul { list-style: none; }
  .about-banner { position: absolute; left: 0; top: 30px; width: 354px; height: 96px; }
  .banner-art {
    position: absolute; left: 60px; top: 0; width: 262px; height: 92px;
    background: radial-gradient(ellipse at 50% 70%, rgba(242,155,192,0.55), rgba(255,255,255,0.35) 45%, rgba(255,255,255,0) 72%);
  }
  .ribbon-band { position: absolute; left: 0; top: 55px; width: 354px; height: 15px; background: var(--ribbon); }
  .about-title {
    position: absolute; left: 60px; top: 8px; width: 262px; text-align: center;
    font-family: "Parisienne", cursive; font-size: 36px; line-height: 44px; color: var(--banner);
  }
  .about-list { position: absolute; left: 16px; top: 154px; width: 320px; }
  .about-list li { padding-left: 7px; text-indent: -7px; }
  .styles { position: absolute; left: 16px; top: 273px; width: 330px; }
  .styles h3.first { margin-top: 1px; }
  .photo { position: absolute; border: 4px solid var(--photo-frame); }
  .photo-classic { left: 16px; top: 666px; width: 162px; height: 130px;
    background: linear-gradient(135deg, #2b2a40 0%, #6a5a8a 45%, #c54a7a 70%, #3b3450 100%); }
  .photo-open { left: 180px; top: 666px; width: 164px; height: 130px;
    background: linear-gradient(135deg, #e8e2dc 0%, #b9a89a 40%, #4a3a38 75%, #8a3a38 100%); }
  .photo-scrapbook { left: 884px; top: 666px; width: 164px; height: 130px;
    background: radial-gradient(circle at 50% 40%, #b98a70 0%, #2e6f86 35%, #1f4f63 70%, #4a2a20 100%); }
  .pkg li { padding-left: 7px; text-indent: -7px; }
  .pkg { margin-top: 16px; }
  .essentials { margin-top: 18px; }
  .essentials ul { width: 160px; }
  .essentials li { padding-left: 5px; text-indent: -5px; }
  .panel-mid h3.first, .panel-right h3.first { margin-top: 0; }
</style>
</head>
<body>
<main class="spread">
  <section class="panel panel-left">
    <div class="about-banner">
      <div class="banner-art" role="img" aria-label="Decorative scroll banner with a pink ribbon bow"></div>
      <div class="ribbon-band"></div>
      <div class="about-title">About Us</div>
    </div>
    <ul class="about-list">
      <li>*"Top Vows Choice" Winner.</li>
      <li>*Five-Star Rated on VowList.com, AisleNotes.com, and LocalStars.</li>
      <li>*Nearly 2,000 happy clients in 6+years of service.</li>
      <li>*Highest Quality Photo Booth Photos available.</li>
      <li>*Experienced Staff of friends and family that care deeply for our business &amp; your happiness.</li>
    </ul>
    <div class="styles">
      <h2>Choose your style of photo booth experience:</h2>
      <h3 class="first">Our Classic Booth</h3>
      <p>At 7'x5' our classic booth stands elegant and spacious. The largest fully enclosed booth on the market, the Classic Booth is designed to look classy in any venue, with a lovely black exterior and your choice of accent curtain to match your event colors and theme. This booth routinely fits entire tables of 10-12 guests at a time with the record being 20.</p>
      <h3>The Open Booth</h3>
      <p>This option becomes more popular each year.<br>The Open Booth consists of an attractive photo booth kiosk and a backdrop of your choosing. While sacrificing the privacy of an enclosed booth, the Open Booth promotes itself, often becoming a spectacle and attracting the entire party to watch in the enjoyment of your other guests. People seem to gravitate toward the Open Booth to watch and inevitably take part in the fun themselves. If you want to get everyone into the spirit and privacy is no issue, this is an excellent choice.</p>
    </div>
    <div class="photo photo-classic" role="img" aria-label="Photo of the enclosed classic booth with pink curtain and red carpet"></div>
    <div class="photo photo-open" role="img" aria-label="Photo of the open booth with a step and repeat backdrop at an event"></div>
  </section>

  <section class="panel panel-mid">
    <h2>Upgrade to a specialty booth- completely unique one of a kind designs</h2>
    <h3 class="first">The Party Booth</h3>
    <p>Our Party Booth is a Pink &amp; Black Damask version of our Classic Booth with a Pink LED lit Photo Booth Kiosk within. This is an excellent choice for Sweet 16's, Quincenera's, and party scenes.</p>
    <h3>The Shore Booth</h3>
    <p>This booth captures a little bit of the sea and brings it to your event. This shimmery Blue version of our Classic Booth comes with ocean themed props, Blue Led lit Photo Kiosk, wooden dock post &amp; rope stanchions and blue carpet. If you are having a shore themed event you need to have this booth.</p>
    <h3>The Saffron Booth</h3>
    <p>This options takes inspiration from Bollywood and Southeast Asia and brings it to our friends here in New Jersey. This option is a lovely Red and Purple, accented with gold, with a purple LED lit kiosk inside. This option is great if you want your photo booth to have some Bollywood flare and also comes with some Bollywood themed Props to make your photos that much more memorable.</p>
    <div class="pkg">
      <h2>Each rental package comes with:</h2>
      <ul>
        <li>*Your Choice of Classic or Open Booth.</li>
        <li>*4 Hour Photo Booth Rental.</li>
        <li>*Professionally, Amazing, and Well Dressed Photo Booth Attendant.</li>
        <li>*High Quality Photography &amp; Lighting for the Finest Photos.</li>
        <li>*(2) 2x6 Photo Strips per session.</li>
        <li>*Your Choice of Backdrop- over 10 colors to choose from.</li>
        <li>*Your Choice of Accent Curtain for Classic Booth rentals.</li>
        <li>*Your Choice of Caption &amp; Style to commemorate your event.</li>
        <li>*Digital Copies of all images.</li>
        <li>*Access to a password protected gallery and free downloads for your guests.</li>
        <li>*Prop Box with all the essentials.</li>
      </ul>
    </div>
  </section>

  <section class="panel panel-right">
    <h2>Upgrades</h2>
    <h3 class="first">The Jazz Age Booth</h3>
    <p>This is a Roaring Twenties themed upgrade- 1920's style props, gold or silver sequin backdrop for your photos, Jazz Age themed kiosk screen. We can also adorn your classic booth rental with a gold curtain if you select this package, giving you that black and gold combo that screams "Jazz Age".</p>
    <h3>The Hollywood</h3>
    <p>This is an upgrade that adds a red carpet, brass stancions, and red velvet rope to your package. Additionally, you will receive a Hollywood Prop upgrade as well.</p>
    <h3>Specialty Booth</h3>
    <p>Upgrade to The Party Booth, The Shore Booth, or The Saffron Booth.</p>
    <h3>Social Media Kiosk</h3>
    <p>Enable your guests to upload their photos straight to FriendSpace, ChirpNet, and their email. This is great for corporate clients wanting to get their branded photos out to the walls of FriendSpace users and of course anyone looking to cater to their guests.</p>
    <h3>Green Screen</h3>
    <p>Insert any backdrop you can think of!</p>
    <h3>Custom Step &amp; Repeat Backdrop</h3>
    <p>A branded or personalized banner is a great way to commemorate an occasion. This combined with the Social Media Kiosk gives our corporate clients an edge in reaching their targeted audience.</p>
    <div class="essentials">
      <h2>Essentials</h2>
      <ul>
        <li>•Double Prints per session</li>
        <li>•Print per Person each session</li>
        <li>•Plastic Sleeves</li>
        <li>•2x6 acrylic frames &amp; 4x6 acrylic frames</li>
        <li>•Placecard Inserts for your Frames</li>
        <li>•Scrapbook</li>
      </ul>
    </div>
  </section>
  <div class="photo photo-scrapbook" role="img" aria-label="Photo of a glittery blue scrapbook with a framed photo strip on the cover"></div>
</main>
</body>
</html>
```